Corporate Personal Training Business needs a flyer for High Scale apartment complex contract

We are looking at getting a flyer for a high scale apartment complex that will explain the prices and services on the back page and offer a complimentary personal training session on the front page as well as a welcome and so on. I will attach plenty of information and also a copy of a basic flyer that does not look very good but will give you an understanding of what I am looking at doing.

Attached I will include all required information as well as pictures I wish to be used in the flyer also and any other information I can think of adding.

Logo design is already done but I am open to suggestion for new logos if you would like to make that part of the project.

The opening day for this project is on Sunday the 14th of July so I do not have a massive amount of time but more then enough to get the project done.

All required pictures can be accessed via the files I have uploaded.

Please note that 72 Kestrel logo needs to be the same as the file I have attached.
Updates

PDF Format of the flyer has been uploaded here you can find logos, photos and information that is required.

All info on the flyer needs to be included just needs to look much more professional. Thankyou

Target Market(s)

Upmarket business people for the most part might have a few young people but generally 35+

Industry/Entity Type

Apartment

Requirements
Must have
• From page one you will see various pictures displaying the types of training I can provide. Kettlebells weights kickboxing etc. These pictures are required unless you feel they will be placed in written form somewhere to make it look better. I liked the idea of making that visual but it is up to you.

The flyer must be 1 page front and back with the front being very attractive to the eye and outlining the complimentary PT session. The info displayed on the front page can be shortened down if necessary as long as the basic idea is projected across and people are aware that the services provided have a wide variety and are fun.

I want the photo of the trainer included as well as the logo above info is also required such as ABN number business name obviously and so on.

Also There needs to be mention that the Owners Corporation will be covering cost of the induction until Jan 2014

Should not have
• A different font with 72 Kestrel the attached image on the flyer is what needs to be used as its the 72 kestrel logo

```html
<!DOCTYPE html>
<html lang="en">
<head>
<meta charset="utf-8">
<title>Pricing and Services Flyer</title>
<link rel="stylesheet" href="https://fonts.googleapis.com/css2?family=Oswald:wght@500;600;700&family=Roboto+Condensed:wght@700&family=Arimo:wght@700&display=swap">
<style>
:root{
  --cyan:#3fc4f0;
  --cyan-text:#34bdf0;
  --ice:#c6edfb;
  --deep:#0f86b9;
  --ink:#111;
  --body:#2a2a2a;
  --white:#fff;
  --rule:#7a8c94;
}
*{margin:0;padding:0;box-sizing:border-box}
html,body{width:927px;height:1200px;overflow:hidden;background:var(--white)}
.flyer{position:relative;width:927px;height:1200px;overflow:hidden;background:var(--white);font-family:'Arimo',Arial,sans-serif;color:var(--body)}
.abs{position:absolute}
.photo{position:absolute}
.photo--cycling{left:0;top:0;width:222px;height:250px;background:linear-gradient(135deg,#d9d2cc,#a99588 55%,#e2a2c0)}
.photo--kickboxing{left:228px;top:0;width:412px;height:265px;background:linear-gradient(120deg,#6fa6c8,#d9a48c 45%,#3ea892 75%,#2a2a2a)}
.photo--measure{left:670px;top:57px;width:223px;height:220px;background:linear-gradient(180deg,#9fb1d6,#c8a89a 50%,#2b2b2b)}
.photo--couple{left:395px;top:955px;width:245px;height:245px;background:linear-gradient(160deg,rgba(230,200,170,.0),#e7c1a3 35%,#6fd0e8 80%)}
.side{left:640px;top:0;width:287px;height:1200px;background:var(--ink)}
.tag{position:absolute;background:var(--cyan);color:var(--white);font-family:'Oswald',sans-serif;font-weight:600;text-transform:uppercase}
.tag--pricing{left:0;top:250px;width:248px;height:42px;font-size:29px;line-height:42px;padding-left:62px}
.tag--services{left:620px;top:308px;width:307px;height:47px;font-size:27px;line-height:47px;padding-left:36px}
.fold{position:absolute;width:0;height:0}
.fold--pricing{left:230px;top:292px;border-top:16px solid #1a7fae;border-left:18px solid transparent}
.fold--services{left:620px;top:355px;border-top:16px solid #1a7fae;border-right:20px solid transparent}
.intro{left:60px;top:315px;width:545px;font-size:13.6px;line-height:18px}
.rate{position:absolute;top:402px;width:112px}
.rate__label{height:32px;background:var(--cyan);border-radius:10px 10px 0 0;font-family:'Oswald',sans-serif;font-weight:500;font-size:19px;line-height:32px;text-align:center;color:var(--ink)}
.rate__price{height:76px;background:var(--ink);border-radius:10px;margin-top:-2px;font-family:'Oswald',sans-serif;font-weight:700;font-size:54px;line-height:76px;text-align:center;color:var(--white);letter-spacing:-1px}
.limit{left:60px;top:526px;font-family:'Roboto Condensed',sans-serif;font-size:21px;color:var(--cyan-text)}
.bullets{list-style:none}
.bullets li{position:relative;padding-left:18px}
.bullets li::before{content:"";position:absolute;left:0;top:5px;width:9px;height:9px;background:var(--cyan)}
.terms{font-size:15.5px;line-height:20px;color:#333}
.terms--left{left:58px;top:565px;width:280px}
.terms--left li+li{margin-top:16px}
.terms--right{left:350px;top:567px;width:270px}
.weekly{left:0;top:655px;width:640px;height:338px;background:var(--ice)}
.weekly__title{position:absolute;left:55px;top:662px;font-family:'Oswald',sans-serif;font-weight:600;font-size:34px;color:var(--ink);letter-spacing:.3px}
.col{position:absolute;top:714px}
.col__head{height:28px;background:var(--ink);color:var(--cyan-text);font-family:'Oswald',sans-serif;font-weight:600;font-size:21px;line-height:28px;padding-left:10px}
.col__list{margin-top:10px;font-size:13.4px;line-height:17px;color:#222}
.col__list li{padding-left:15px}
.col__list li::before{top:4px;width:7px;height:7px}
.col__list li+li{margin-top:14px}
.col--one{left:55px;width:162px}
.col--two{left:253px;width:158px}
.col--three{left:447px;width:173px}
.divider{position:absolute;top:714px;width:1px;height:264px;background:var(--rule)}
.group__band{left:0;top:993px;width:640px;height:42px;background:var(--cyan);color:var(--white);font-family:'Oswald',sans-serif;font-weight:500;font-size:22px;line-height:42px;padding-left:55px}
.group__body{left:0;top:1035px;width:640px;height:165px;background:var(--deep)}
.group__table{position:absolute;left:55px;top:1050px;border-collapse:collapse;font-family:'Roboto Condensed',sans-serif;font-size:19px;color:var(--white)}
.group__table td{padding:0;height:25px}
.group__table td:first-child{width:120px}
.group__brace{left:214px;top:1050px}
.group__note{left:272px;top:1101px;font-family:'Arimo',sans-serif;font-weight:400;font-size:17px;line-height:23px;color:var(--white)}
.services{left:670px;top:388px;width:230px;font-family:'Roboto Condensed',sans-serif}
.service__title{font-size:21px;line-height:25px;color:var(--cyan-text)}
.service__text{margin-top:10px;margin-bottom:14px;font-size:16.6px;line-height:22.5px;color:var(--white)}
</style>
</head>
<body>
<div class="flyer">
  <div class="photo photo--cycling" role="img" aria-label="Women riding exercise bikes in a spin class"></div>
  <div class="photo photo--kickboxing" role="img" aria-label="Woman in boxing gloves throwing a kick at a trainer's pad in a gym"></div>
  <div class="abs side"></div>
  <div class="photo photo--measure" role="img" aria-label="Slim waist wrapped in a yellow measuring tape"></div>

  <div class="tag tag--pricing">Pricing</div>
  <div class="fold fold--pricing"></div>

  <p class="abs intro">Inductions: This service is required to receive access to the gym facility and ensures that the equipment will be used correctly and safely. You will be shown correct technique, how to use and adjust the machines as needed and also be shown some ideas and exercises specific to your own goals.</p>

  <div class="rate" style="left:60px"><div class="rate__label">1 Person</div><div class="rate__price">$30</div></div>
  <div class="rate" style="left:188px"><div class="rate__label">2 People</div><div class="rate__price">$50</div></div>
  <div class="rate" style="left:316px"><div class="rate__label">3 People</div><div class="rate__price">$70</div></div>
  <div class="rate" style="left:444px"><div class="rate__label">4 People</div><div class="rate__price">$80</div></div>

  <p class="abs limit">Limited to a total of 4 people per session</p>

  <ul class="abs bullets terms terms--left">
    <li>One on One Personal Training 45 Minute sessions</li>
    <li>Rate: $50 per session</li>
  </ul>
  <ul class="abs bullets terms terms--right">
    <li>The Owners Corporation will be covering the cost of all inductions until Jan 2014</li>
  </ul>

  <div class="abs weekly"></div>
  <h2 class="weekly__title">TRAINING PER WEEK</h2>

  <div class="col col--one">
    <div class="col__head">1 TIME</div>
    <ul class="bullets col__list">
      <li>Individually tailored program design plus full accountability for effective self training.</li>
      <li>Full Nutrition program design based on individuals goals</li>
      <li>Fitness Assessment and Wellness Evaluation.</li>
    </ul>
  </div>
  <div class="divider" style="left:235px"></div>
  <div class="col col--two">
    <div class="col__head">2 TIMES</div>
    <ul class="bullets col__list">
      <li>All the above benefits including the following.</li>
      <li>50 % Off all New Stridewell Clothing and Shoes Access to the trainers Personal nutrition plan where he lost 10 kilos and went from 12% to 8% body fat in 12 weeks.</li>
    </ul>
  </div>
  <div class="divider" style="left:432px"></div>
  <div class="col col--three">
    <div class="col__head">3 TIMES OR MORE</div>
    <ul class="bullets col__list">
      <li>All the above benefits including the following</li>
      <li>Only $45 per session when you commit to one months training</li>
      <li>A complimentary gift valued at $70 with the one month commitment</li>
    </ul>
  </div>

  <div class="abs group__band">Group Training: 45 minute sessions</div>
  <div class="abs group__body"></div>
  <table class="group__table">
    <tr><td>2 People</td><td>$35</td></tr>
    <tr><td>3 People</td><td>$25</td></tr>
    <tr><td>4 People</td><td>$20</td></tr>
    <tr><td>5 - 9 People</td><td>$15</td></tr>
    <tr><td>10+</td><td>$10</td></tr>
  </table>
  <svg class="abs group__brace" width="40" height="130" viewBox="0 0 40 130" aria-hidden="true">
    <path d="M4 3 Q22 3 22 20 L22 52 Q22 65 36 65 Q22 65 22 78 L22 110 Q22 127 4 127" fill="none" stroke="#fff" stroke-width="3"/>
  </svg>
  <p class="abs group__note">EACH PER<br>SESSION</p>
  <div class="photo photo--couple" role="img" aria-label="Smiling couple in workout clothes, woman holding a pink dumbbell"></div>

  <div class="tag tag--services">Services Provided</div>
  <div class="fold fold--services"></div>

  <div class="abs services">
    <h3 class="service__title">Program Design &amp;<br>Implementation: $150</h3>
    <p class="service__text">Would like to train on your own but not sure how? Full program design plus a session to explain all the exercises you are unsure of.</p>
    <h3 class="service__title">Self Defense &amp;<br>Martial Arts Training</h3>
    <p class="service__text">Get even more out of your PT sessions and get lean and fit while learning how to defend yourself with various styles of Martial Arts Training. Learning skills from Taekwondo, Muay Thai Kickboxing, Boxing and Brazilian Jiu Jitsu</p>
    <h3 class="service__title">Losing Weight,<br>Increasing Fitness,<br>Gaining Lean Muscle</h3>
    <p class="service__text">An assessment of your goals, measurements and training interests will be done prior to training to ensure you achieve the maximum benefit from your sessions regardless of what your health and fitness goals may be.</p>
  </div>
</div>
</body>
</html>
```